Judicial election website to attract voters

I need a simple one-page web design for a judicial election. I'm going to put up one picture, maybe two. The picture I have needs a little touch-up (whiten teeth for example). I have 3 paragraphs of text. I'd like a "Donate" button that can link to a CoinDrift account. I'd also like a little background design, like the Constitution or something like that. There's a couple other little things but that's the bulk of it.

Target Market(s)

Involved voters and some media

Industry/Entity Type

Legal

Number of Pages Required

1 page

Font styles to use
Sans Serif

Requirements
Must have
• My picture, text, donate button
• Phrase "Remember to vote August 30, 2016!"
Nice to have
• Perhaps a second photo, maybe a short 30 second video of me talking directly to the voters, cool background: Constitution, something judgey.
Should not have
• Not sure ... profanity, I guess.

```html
<!DOCTYPE html>
<html lang="en">
<head>
<meta charset="utf-8">
<title>Rosalind for Judge</title>
<link href="https://fonts.googleapis.com/css2?family=Cinzel:wght@400&family=Open+Sans:ital,wght@0,400;0,600;0,700;1,600&display=swap" rel="stylesheet">
<style>
  :root {
    --brand-blue: #1a22c8;
    --white: #ffffff;
    --ink: #333333;
    --footer-bg: #2a2a2b;
    --button-dark: #2c2c2c;
    --frame: #555555;
  }
  * { margin: 0; padding: 0; box-sizing: border-box; }
  html, body { width: 1200px; height: 1002px; overflow: hidden; background: var(--white); }
  body { position: relative; font-family: "Open Sans", Arial, sans-serif; }

  .hero { position: absolute; left: 0; top: 0; width: 1200px; height: 537px; overflow: hidden; }
  .hero-photo {
    position: absolute; inset: 0;
    background:
      linear-gradient(180deg, rgba(60,64,74,.55) 0%, rgba(70,72,78,.35) 55%, rgba(40,40,42,.55) 100%),
      linear-gradient(180deg, #6f7482 0%, #7b7c80 45%, #8a8476 70%, #4a4a46 100%);
  }
  .menu-icon { position: absolute; left: 1077px; top: 61px; }
  .candidate-name {
    position: absolute; left: 0; width: 1200px; top: 156px; text-align: center;
    font-family: "Cinzel", Georgia, serif; font-size: 39px; color: var(--brand-blue); letter-spacing: 1px;
  }
  .vote-reminder {
    position: absolute; left: 0; width: 1200px; top: 244px; text-align: center;
    font-weight: 700; font-size: 37px; color: var(--white); text-transform: uppercase;
  }
  .qualities {
    position: absolute; left: 0; width: 1200px; top: 303px; text-align: center;
    font-style: italic; font-weight: 600; font-size: 32px; color: var(--white);
  }
  .qualities .dot { font-style: normal; font-size: 18px; margin: 0 24px; vertical-align: middle; }
  .play-button { position: absolute; left: 553px; top: 380px; }
  .slide-arrow { position: absolute; top: 262px; }
  .slide-arrow.prev { left: 46px; }
  .slide-arrow.next { left: 1144px; }

  .about { position: absolute; left: 99px; top: 598px; width: 640px; }
  .about h2 { font-weight: 400; font-size: 27px; color: var(--brand-blue); }
  .about p { margin-top: 22px; font-size: 12.6px; line-height: 30px; color: var(--ink); }
  .actions { position: absolute; left: 98px; top: 829px; display: flex; gap: 23px; }
  .btn {
    display: inline-flex; align-items: center; justify-content: center; height: 36px;
    font-weight: 600; font-size: 16px; color: var(--white); text-decoration: none;
    box-shadow: 2px 2px 3px rgba(0,0,0,.45);
  }
  .btn-read { width: 115px; background: linear-gradient(180deg, #2a32e0, #1419b0); }
  .btn-donate { width: 142px; background: linear-gradient(180deg, #3c3c3c, #1e1e1e); }
  .portrait {
    position: absolute; left: 782px; top: 570px; width: 319px; height: 326px;
    border: 3px solid var(--frame);
    background: linear-gradient(160deg, #dcdde0 0%, #c9b8a6 45%, #d89680 80%, #e88a66 100%);
  }

  .site-footer { position: absolute; left: 0; top: 928px; width: 1200px; height: 74px; background: var(--footer-bg); }
  .copyright {
    position: absolute; left: 99px; top: 27px; display: flex; align-items: center; gap: 8px;
    font-size: 12.6px; color: var(--white);
  }
  .social { position: absolute; left: 920px; top: 17px; display: flex; gap: 10px; }
</style>
</head>
<body>
  <header class="hero">
    <div class="hero-photo" role="img" aria-label="Dusk photograph of a large civic monument with winged pillars on a city square"></div>
    <svg class="menu-icon" width="20" height="18" viewBox="0 0 20 18" aria-label="Menu">
      <rect x="0" y="0" width="20" height="4" rx="1" fill="#fff"/>
      <rect x="0" y="7" width="20" height="4" rx="1" fill="#fff"/>
      <rect x="0" y="14" width="20" height="4" rx="1" fill="#fff"/>
    </svg>
    <h1 class="candidate-name">ROSALIND</h1>
    <p class="vote-reminder">Remember to vote August 30, 2016!</p>
    <p class="qualities">Experience<span class="dot">•</span>Dedicated<span class="dot">•</span>Respected</p>
    <svg class="play-button" width="92" height="92" viewBox="0 0 92 92" aria-label="Play video">
      <circle cx="46" cy="46" r="43" fill="none" stroke="#fff" stroke-width="3"/>
      <path d="M37 29 L63 46 L37 63 Z" fill="none" stroke="#fff" stroke-width="3" stroke-linejoin="round"/>
    </svg>
    <svg class="slide-arrow prev" width="14" height="28" viewBox="0 0 14 28" aria-label="Previous slide">
      <path d="M11 4 L4 14 L11 24" fill="none" stroke="#fff" stroke-width="2.5"/>
    </svg>
    <svg class="slide-arrow next" width="14" height="28" viewBox="0 0 14 28" aria-label="Next slide">
      <path d="M3 4 L10 14 L3 24" fill="none" stroke="#fff" stroke-width="2.5"/>
    </svg>
  </header>

  <main>
    <section class="about">
      <h2>About Our Rosalind</h2>
      <p>Rosalind was born and raised in Tampa Florida, the daughter of an air-conditioning repairman who later opened his own successful business. As the first in her family to go to college, her parents could not have been more proud as she finished her degree at Gulf Coast University, then continued on to Sunbelt State College of Law where she graduated with honors. Dedicating her life to public service in central Florida, she has spent the last 18 years as a prosecutor fighting for victims of child abuse and sexual abuse</p>
    </section>
    <div class="actions">
      <a class="btn btn-read" href="#">Read More</a>
      <a class="btn btn-donate" href="#">Donate Now</a>
    </div>
    <div class="portrait" role="img" aria-label="Portrait photograph of the candidate"></div>
  </main>

  <footer class="site-footer">
    <div class="copyright">
      <svg width="14" height="14" viewBox="0 0 14 14" aria-hidden="true">
        <circle cx="7" cy="7" r="6" fill="none" stroke="#fff" stroke-width="1.5"/>
        <path d="M9.3 5.2 A3 3 0 1 0 9.3 8.8" fill="none" stroke="#fff" stroke-width="1.5"/>
      </svg>
      <span>Companyname 2016 . All Rights Reserved</span>
    </div>
    <div class="social">
      <svg width="38" height="38" viewBox="0 0 38 38" aria-label="Social link"><circle cx="19" cy="19" r="17.5" fill="none" stroke="#fff" stroke-width="2"/></svg>
      <svg width="38" height="38" viewBox="0 0 38 38" aria-label="Social link"><circle cx="19" cy="19" r="17.5" fill="none" stroke="#fff" stroke-width="2"/></svg>
      <svg width="38" height="38" viewBox="0 0 38 38" aria-label="News feed link"><circle cx="19" cy="19" r="17.5" fill="none" stroke="#fff" stroke-width="2"/></svg>
      <svg width="38" height="38" viewBox="0 0 38 38" aria-label="Social link"><circle cx="19" cy="19" r="17.5" fill="none" stroke="#fff" stroke-width="2"/></svg>
    </div>
  </footer>
</body>
</html>
```